Coffee bag stamp design for new coffee brand

Stamp design that will be used like a label on a coffee package.
It must be a vector that can be produced as a stamp. Coffee bag is from brown craft paper. I upload image of this bag. Size of design is 80mm x 140mm.
I also uploaded two pictures for inspiration, but I will also appreciate new ideas.

Target Market(s)

Coffee lovers, who love to try new coffee. Also hipsters.

Colors

Designer to choose only greyscale colors for use in the design.

Requirements
Must have
• Some information about coffee must have:
Name: BRAZIL (the biggest font in that design)
Region: Santos
Altitude: 60 – 1200 m.n.m.
Variety: Arabica
Processing: unwashed

```html
<!DOCTYPE html>
<html lang="en">
<head>
<meta charset="utf-8">
<title>Lotara Coffee – Brazil label</title>
<link href="https://fonts.googleapis.com/css2?family=Bebas+Neue&family=Courier+Prime:wght@700&family=Josefin+Sans:wght@700&family=Lobster&display=swap" rel="stylesheet">
<style>
  :root {
    --ink: #111111;
    --paper: #ffffff;
    --backdrop: #cbcbcb;
    --bean-tone: #2a2a2a;
    --shadow: rgba(0, 0, 0, 0.35);
  }
  * { margin: 0; padding: 0; box-sizing: border-box; }
  html, body {
    width: 1200px;
    height: 923px;
    overflow: hidden;
    background: var(--backdrop);
  }
  .canvas {
    position: relative;
    width: 1200px;
    height: 923px;
  }
  .label {
    position: absolute;
    left: 360px;
    top: 41px;
    width: 480px;
    height: 840px;
    background: var(--paper);
    box-shadow: 6px 6px 8px var(--shadow);
    color: var(--ink);
  }
  .brand {
    position: absolute;
    left: 110px;
    top: 108px;
    width: 260px;
    height: 260px;
    border: 6px solid var(--ink);
    border-radius: 50%;
    display: flex;
    flex-direction: column;
    align-items: center;
    justify-content: center;
  }
  .brand-name {
    font-family: "Josefin Sans", sans-serif;
    font-weight: 700;
    font-size: 40px;
    line-height: 1.05;
    letter-spacing: 2px;
    text-align: center;
    color: var(--ink);
    padding-top: 60px;
  }
  .beans {
    position: absolute;
    background: var(--bean-tone);
    border-radius: 40%;
  }
  .beans-left { left: 33px; top: 362px; width: 72px; height: 68px; }
  .beans-right { left: 356px; top: 480px; width: 82px; height: 55px; }
  .product-name {
    position: absolute;
    left: 42px;
    top: 400px;
    font-family: "Lobster", cursive;
    font-size: 138px;
    line-height: 1;
    color: var(--ink);
    text-shadow: 4px 4px 0 var(--paper), 6px 6px 0 var(--ink);
  }
  .specs {
    position: absolute;
    left: 36px;
    top: 556px;
    width: 408px;
    border-collapse: collapse;
    border-top: 4px solid var(--ink);
  }
  .specs td {
    height: 53px;
    border-bottom: 4px solid var(--ink);
    vertical-align: middle;
  }
  .specs .spec-label {
    width: 183px;
    font-family: "Courier Prime", monospace;
    font-weight: 700;
    font-size: 20px;
    border-right: 3px dotted var(--ink);
    white-space: nowrap;
  }
  .specs .spec-label::before {
    content: "";
    display: inline-block;
    width: 8px;
    height: 13px;
    margin: 0 6px 0 2px;
    border-radius: 50%;
    background: var(--ink);
    vertical-align: -1px;
  }
  .specs .spec-value {
    padding-left: 14px;
    font-family: "Bebas Neue", sans-serif;
    font-size: 32px;
    padding-top: 4px;
  }
  .specs-rule {
    position: absolute;
    left: 36px;
    top: 774px;
    width: 408px;
    height: 8px;
    border-top: 3px dotted var(--ink);
    border-bottom: 3px solid var(--ink);
  }
</style>
</head>
<body>
<main class="canvas">
  <section class="label">
    <div class="brand">
      <p class="brand-name">LOTARA<br>COFFEE</p>
    </div>
    <div class="beans beans-left" role="img" aria-label="Illustration of scattered coffee beans"></div>
    <div class="beans beans-right" role="img" aria-label="Illustration of scattered coffee beans"></div>
    <h1 class="product-name">Brazil</h1>
    <table class="specs">
      <tr><td class="spec-label">Region</td><td class="spec-value">Santos</td></tr>
      <tr><td class="spec-label">Altitude</td><td class="spec-value">60 – 1200 M.N.M.</td></tr>
      <tr><td class="spec-label">Variety</td><td class="spec-value">Arabica</td></tr>
      <tr><td class="spec-label">Processing</td><td class="spec-value">Unwashed</td></tr>
    </table>
    <div class="specs-rule"></div>
  </section>
</main>
</body>
</html>
```